依頼詳細
不動産物件情報の冊子の表紙デザインです。5月らしいイメージと、簡単には捨てられないインパクトのあるデザインをお願いします。
会社WEB:http://morinaga-hoshizora.jp/
記載項目
タイトル「物件情報 2019 5月号」 会社ロゴ:添付参照
希望イメージ
シンプル 複雑
単色 カラフル
暗い 明るい
日常 高級
遊び心 厳粛
未来的 伝統的
女性的 男性的
希望する色
納品ファイル
• イラストレーター形式 (.ai)
補足説明
四半期に一度発行予定ですので、継続の可能性もあります
参考までに新春号のデータを添付いたします
先述の、物件情報は、関東・九州の情報が主ですが、全国の情報を掲載しております。
■ 選んだ理由

弊社の意図をよくご理解いただき、季節に合ったご提案をいただきました。データ化の対応も迅速な対応で、助かりました。引き続きよろしくお願いします

■ 提案者全員のお礼・コメント

たくさんのご提案をいただき、参加いただいた皆様には深謝いたします。
どのご提案も、素晴らしいものでした。

次号は夏ごろを予定しておりますので、その折には、また多くの方々のご提案をいただくことができればと存じます。
今後ともよろしくお願いいたします

```html
<!DOCTYPE html>
<html lang="ja">
<head>
<meta charset="utf-8">
<title>物件情報 2019 5月号</title>
<link rel="stylesheet" href="https://fonts.googleapis.com/css2?family=M+PLUS+Rounded+1c:wght@500;800&display=swap">
<style>
  :root {
    --tile-pink: #e9a493;
    --tile-mint: #bfdcb7;
    --tile-aqua: #66c3d4;
    --tile-cream: #eee6d4;
    --title-brown: #7d5a3c;
    --outline-white: #ffffff;
    --brand-ink: #3e4a3a;
  }
  * { margin: 0; padding: 0; box-sizing: border-box; }
  html, body { width: 822px; height: 1200px; overflow: hidden; background: #ffffff; }
  .cover {
    position: relative;
    width: 822px;
    height: 1200px;
    overflow: hidden;
    font-family: "M PLUS Rounded 1c", sans-serif;
  }
  .tile-backdrop {
    position: absolute;
    inset: 0;
    background:
      radial-gradient(circle at 12% 50%, rgba(102,195,212,0.85) 0 10%, transparent 22%),
      radial-gradient(circle at 66% 68%, rgba(102,195,212,0.85) 0 9%, transparent 20%),
      radial-gradient(circle at 30% 20%, rgba(233,164,147,0.7) 0 10%, transparent 24%),
      radial-gradient(circle at 80% 40%, rgba(233,164,147,0.7) 0 12%, transparent 26%),
      radial-gradient(circle at 20% 85%, rgba(233,164,147,0.6) 0 12%, transparent 26%),
      radial-gradient(circle at 85% 90%, rgba(191,220,183,0.8) 0 12%, transparent 28%),
      linear-gradient(160deg, var(--tile-mint), var(--tile-cream) 45%, var(--tile-pink) 80%, var(--tile-mint));
  }
  .cover-art { position: absolute; inset: 0; }
  .title-char {
    font-weight: 800;
    font-size: 168px;
    fill: var(--title-brown);
    stroke: var(--outline-white);
    stroke-width: 10px;
    paint-order: stroke;
    stroke-linejoin: round;
  }
  .year, .issue-num, .issue-suffix {
    font-weight: 800;
    fill: var(--outline-white);
  }
  .year { font-size: 50px; }
  .issue-num { font-size: 92px; }
  .issue-suffix { font-size: 38px; }
  .brand-name {
    font-weight: 800;
    font-size: 30px;
    fill: var(--brand-ink);
  }
  .brand-dot { fill: var(--brand-ink); }
</style>
</head>
<body>
  <main class="cover">
    <div class="tile-backdrop" role="img" aria-label="Glossy ceramic tiles in pink, mint green and aqua laid in a grid"></div>
    <svg class="cover-art" viewBox="0 0 822 1200" width="822" height="1200">
      <g class="title">
        <text class="title-char" x="178" y="295">物</text>
        <text class="title-char" x="408" y="295">件</text>
        <text class="title-char" x="178" y="530">情</text>
        <text class="title-char" x="408" y="530">報</text>
      </g>
      <text class="year" x="40" y="535">2019</text>
      <g class="brand">
        <circle class="brand-dot" cx="384" cy="690" r="22"/>
        <text class="brand-name" x="384" y="762" text-anchor="middle">Hoshizora</text>
      </g>
      <g class="issue">
        <text class="issue-num" x="480" y="850">5</text>
        <text class="issue-suffix" x="538" y="850">月号</text>
      </g>
    </svg>
  </main>
</body>
</html>
```